Business card for our large format printing and installation business

We want a professional looking business card for our business. We manufacture and install Signs.

On the back of the card add this info
Large Format Graphics Printing & Installations, Event Graphics, Banners, Posters, Vehicle Fleet Graphics, Boat Wraps, Wall Murals, Decals,Displays,Signs,Plaques,Digital Signs

On the Front of the card add the Tallowfern Signs logo, plus On the back of the card add the Orange Tallowfern Wraps logo. The 2 vector logos are attached to the design brief.

Target Market(s)

Local business owners

Contact Information for Business Card

Colors
f37122
f68d4e
f9ba93

Requirements
Must have
• On the Front of the card add the Tallowfern Signs logo, plus On the back of the card add the Orange Tallowfern Wraps logo. The 2 vector logos are attached to the design brief.

```html
<!DOCTYPE html>
<html lang="en">
<head>
<meta charset="utf-8">
<title>Tallowfern Signs business card</title>
<link rel="stylesheet" href="https://fonts.googleapis.com/css2?family=Roboto:wght@400;700;900&display=swap">
<style>
  :root {
    --backdrop: #d9d8d8;
    --card-white: #ffffff;
    --card-black: #1d1d1d;
    --orange: #f6a823;
    --orange-deep: #f37122;
    --orange-soft: #f9ba93;
    --faint: #ece7dc;
    --text-light: #f2f2f2;
  }
  * { margin: 0; padding: 0; box-sizing: border-box; }
  html, body { width: 1200px; height: 807px; overflow: hidden; }
  body {
    background: var(--backdrop);
    font-family: "Roboto", Arial, sans-serif;
    position: relative;
  }
  .card {
    position: absolute;
    top: 258px;
    width: 500px;
    height: 290px;
    overflow: hidden;
    box-shadow: 0 6px 18px rgba(0,0,0,0.18);
  }
  .card--front { left: 70px; background: var(--card-white); }
  .card--back { left: 630px; background: var(--card-black); }

  .front-panel {
    position: absolute; left: 0; top: 0; width: 400px; height: 172px;
    background: var(--card-black);
  }
  .front-rule {
    position: absolute; left: 0; top: 172px; width: 400px; height: 12px;
    background: var(--orange);
  }
  .brand-name {
    position: absolute; left: 34px; top: 26px;
    font-weight: 900; font-size: 30px; color: var(--orange); letter-spacing: 0.5px;
  }
  .person { position: absolute; left: 34px; top: 76px; }
  .person-name { font-size: 19px; color: var(--orange); letter-spacing: 1px; }
  .person-role { font-size: 14px; color: var(--text-light); margin-top: 2px; }

  .contact-block {
    position: absolute; left: 210px; top: 104px; width: 270px; height: 150px;
    background: var(--orange);
  }
  .contact-divider {
    position: absolute; left: 0; top: 64px; width: 270px; height: 12px;
    background: var(--card-black);
  }
  .contact-row {
    position: absolute; left: 16px; right: 14px;
    display: flex; justify-content: space-between; align-items: center;
    font-size: 13px; color: var(--card-black);
  }
  .contact-row svg { width: 14px; height: 14px; }
  .row-1 { top: 12px; } .row-2 { top: 36px; }
  .row-3 { top: 88px; } .row-4 { top: 114px; }

  .brand-ghost {
    position: absolute; left: 30px; top: 222px;
    font-weight: 900; font-size: 19px; color: var(--faint);
  }

  .back-content {
    position: absolute; left: 40px; right: 40px; top: 50%; transform: translateY(-50%);
    text-align: center;
  }
  .back-brand { font-weight: 900; font-size: 40px; color: var(--orange); }
  .back-wraps { font-weight: 900; font-size: 22px; color: var(--orange-deep); margin-top: 6px; }
  .back-rule { width: 120px; height: 3px; background: var(--orange); margin: 14px auto 12px; }
  .services { font-size: 11.5px; line-height: 1.6; color: var(--text-light); }
</style>
</head>
<body>
  <section class="card card--front" aria-label="Card front">
    <div class="front-panel"></div>
    <div class="front-rule"></div>
    <div class="brand-name">Tallowfern Signs</div>
    <div class="person">
      <div class="person-name">Marla Quint</div>
      <div class="person-role">founder&amp;CEO</div>
    </div>
    <div class="contact-block">
      <div class="contact-divider"></div>
      <div class="contact-row row-1"><span>+0155 208 316 942</span>
        <svg viewBox="0 0 14 14"><circle cx="7" cy="7" r="7" fill="#1d1d1d"/><path d="M4.5 4c.5 2.5 2.5 4.8 5 5.5l.8-1-1.3-.8-.6.6C7.3 7.8 6.3 6.8 5.8 5.7l.6-.6-.8-1.3z" fill="#f6a823"/></svg></div>
      <div class="contact-row row-2"><span>+0166 412 730 581</span>
        <svg viewBox="0 0 14 14"><circle cx="7" cy="7" r="7" fill="#1d1d1d"/><path d="M4.5 4c.5 2.5 2.5 4.8 5 5.5l.8-1-1.3-.8-.6.6C7.3 7.8 6.3 6.8 5.8 5.7l.6-.6-.8-1.3z" fill="#f6a823"/></svg></div>
      <div class="contact-row row-3"><span>info@tallowfern.com</span>
        <svg viewBox="0 0 14 14"><circle cx="7" cy="7" r="7" fill="#1d1d1d"/><rect x="3.8" y="4.8" width="6.4" height="4.4" fill="none" stroke="#f6a823" stroke-width="0.9"/><path d="M3.8 4.8 7 7.3l3.2-2.5" fill="none" stroke="#f6a823" stroke-width="0.9"/></svg></div>
      <div class="contact-row row-4"><span>www.tallowfern.com</span>
        <svg viewBox="0 0 14 14"><circle cx="7" cy="7" r="7" fill="#1d1d1d"/><circle cx="7" cy="7" r="3.4" fill="none" stroke="#f6a823" stroke-width="0.8"/><path d="M3.6 7h6.8M7 3.6c-1.6 2-1.6 4.8 0 6.8M7 3.6c1.6 2 1.6 4.8 0 6.8" fill="none" stroke="#f6a823" stroke-width="0.8"/></svg></div>
    </div>
    <div class="brand-ghost" aria-hidden="true">Tallowfern Signs</div>
  </section>

  <section class="card card--back" aria-label="Card back">
    <div class="back-content">
      <div class="back-brand">Tallowfern Signs</div>
      <div class="back-wraps">Tallowfern Wraps</div>
      <div class="back-rule"></div>
      <p class="services">Large Format Graphics Printing &amp; Installations, Event Graphics, Banners, Posters, Vehicle Fleet Graphics, Boat Wraps, Wall Murals, Decals, Displays, Signs, Plaques, Digital Signs</p>
    </div>
  </section>
</body>
</html>
```